Looking for a cutting-edge design for a healthy, all-nautural dog treats package

We are launching an All-Natural dog treat. It is made of 5 simple ingredients (peanut butter, sweet potatoes, potato flour, flaxseed oil & eggs). This product is white-labeled (meaning the original manufacturer will be producing them for us under our own name). The brand name is TrailPaw.

What We Are Looking For:
We are looking for an approach that really emphasizes the fact that it will be all-natural, grain-free. In fact, we are looking for a design that is very similar to the qv loaf (please take a look at qvloaf.example for examples).

Other Details to Remember:
Attached is a png file of the dimensions provided by the original manufacturer. Please note that our bag will the a "brown paper bag" color. Finally, the back of the bag should include the same verbiage as the original (although does not have to be the same design/fonts).

Project Deadline Extended Reason: It appears that the package can now only be in one color on "brown paper bag" of "off white" packaging. Added Wednesday, October 26, 2016

Target Market(s)

Dog owners that appreciate quality food for their pets...more than likely, they are foodies themselves and/or health conscience

Industry/Entity Type

Pet

Logo Text

TrailPaw

Requirements
Must have
• Emphasis on the product being all-natural, grain-free. Looks similar to the qvloaf packaging (qvloaf.example)
• **IMPORTANT UPDATE**
• The packaging people have notified us that all graphics or lettering must be in ONE SAME COLOR. The package itself will be in either "brown paper bag" or "off white" color.
Should not have
• That being said, please do NOT make it look absolutely identical to the qv loaf

```html
<!DOCTYPE html>
<html lang="en">
<head>
<meta charset="utf-8">
<title>TrailPaw – Natural Dog Treat</title>
<link rel="stylesheet" href="https://fonts.googleapis.com/css2?family=Anton&family=Archivo+Black&family=Roboto+Condensed:wght@700&display=swap">
<style>
  :root {
    --kraft: #c39468;
    --ink: #221b15;
  }
  * { margin: 0; padding: 0; box-sizing: border-box; }
  html, body { width: 906px; height: 1200px; overflow: hidden; }
  body { background: var(--kraft); position: relative; font-family: "Anton", sans-serif; color: var(--ink); }

  .label-frame {
    position: absolute; left: 143px; top: 180px; width: 620px; height: 900px;
    border: 6px solid var(--ink); border-radius: 32px;
  }
  .brand-tab {
    position: absolute; left: 119px; top: -96px; width: 382px; height: 181px;
    background: var(--ink); border-radius: 50%;
    display: flex; align-items: center; justify-content: center;
  }
  .brand-name {
    font-family: "Roboto Condensed", sans-serif; font-weight: 700;
    font-size: 62px; color: var(--kraft); letter-spacing: -0.5px;
  }
  .category-pill {
    position: absolute; left: 47px; top: 127px; width: 91px; height: 647px;
    background: var(--ink); border-radius: 46px;
    display: flex; align-items: center; justify-content: center;
  }
  .category-text {
    font-family: "Archivo Black", sans-serif; font-size: 44px; color: var(--kraft);
    transform: rotate(-90deg); white-space: nowrap; letter-spacing: 1px;
  }
  .claim-badge {
    position: absolute; left: 254px; top: 138px; width: 238px; height: 51px;
    background: var(--ink); border-radius: 26px;
    display: flex; align-items: center; justify-content: center;
    font-size: 36px; color: var(--kraft); line-height: 1;
  }
  .ingredient-list {
    position: absolute; left: 168px; top: 208px; width: 410px; list-style: none;
  }
  .ingredient {
    height: 115px; display: flex; align-items: center; justify-content: center;
    border-bottom: 5px solid var(--ink);
    font-size: 62px; line-height: 1; transform: scaleY(1.05);
  }
  .ingredient:first-child { height: 106px; }
  .net-weight {
    position: absolute; left: 168px; width: 410px; top: 828px; text-align: center;
    font-family: "Roboto Condensed", sans-serif; font-weight: 700; font-size: 25px;
  }
</style>
</head>
<body>
  <section class="label-frame">
    <div class="brand-tab"><span class="brand-name">TrailPaw</span></div>
    <div class="category-pill"><span class="category-text">NATURAL DOG TREAT</span></div>
    <div class="claim-badge">GRAIN FREE</div>
    <ul class="ingredient-list">
      <li class="ingredient">PEANUT BUTTER</li>
      <li class="ingredient">SWEET POTATOES</li>
      <li class="ingredient">POTATO FLOUR</li>
      <li class="ingredient">FLAXSEED OIL</li>
      <li class="ingredient">EGGS</li>
    </ul>
    <p class="net-weight">NET WT. 1.83 OZ (52g)</p>
  </section>
</body>
</html>
```